Facebook Ads for HOA Law Firm

We need to create certain ads for a Facebook ads campaign. We are a law firm in Florida that represents homeowners against HOAs. We need to create the following ads:

1. Image Ads Specifications:

File Type: JPG or PNG
Ratio: 1.91:1 to 4:5
Resolution:
a) 1:1 ratio: 1080 x 1080 pixels
b) 4:5 ratio: 1080 x 1350 pixels
Maximum File Size: 30MB
Minimum Width: 600 pixels
Minimum Height:
a) 1:1 ratio: 600 pixels
b) 4:5 ratio: 750 pixels
Key Elements to Include in the Ads:

1) Headline: "HOA Violating Your Rights?"
2) Main Message: "We sue HOAs for Homeowners."
3) Firm Name: Lindqvist Harrow, P.A.
4) Website: www.brightgatelegal-example.com
5) Phone Number: 1-800-555-0142
6) Florida Bar Compliance Statement: "Serving Homeowners in Florida with our main office in Miami-Dade."
7) Call-to-Action (CTA): Include a strong CTA such as “Contact us today for a consultation!”
8) Tone and Style: Professional yet approachable. The ad should emphasize trust, expertise, and our dedication to homeowners' rights.
9) Branding: Please use our firm's brand colors and fonts. Ensure that our logo is prominently placed within the ad.
10) Image Suggestions: Consider using images of Florida homes, frustrated homeowners, or visuals that evoke trust, protection, and legal authority.

```html
<!DOCTYPE html>
<html lang="en">
<head>
<meta charset="utf-8">
<title>HOA Rights Ad – Size Presentation</title>
<link rel="stylesheet" href="https://fonts.googleapis.com/css2?family=Jost:wght@500;600;700&family=Poppins:ital,wght@0,400;0,500;0,600;0,700;1,800&display=swap">
<style>
  :root{
    --board:#737373;
    --navy-deep:#060a4c;
    --navy:#12149a;
    --brand-blue:#14179a;
    --lavender:#dcdcf6;
    --pill:#6c70d2;
    --quote-line:#7d82ec;
    --ink:#1c1c1c;
    --white:#ffffff;
    --photo-light:#d9d9d9;
    --photo-dark:#5a5a5a;
  }
  *{box-sizing:border-box;margin:0;padding:0}
  html,body{width:1200px;height:1200px;overflow:hidden;background:var(--board)}
  .board{position:relative;width:1200px;height:1200px}
  .ad-card{position:absolute;background:var(--white);box-shadow:0 10px 22px rgba(0,0,0,.35)}
  .ad-card svg{display:block;width:100%;height:100%}
  .ad-card--square{left:367px;top:62px;width:466px;height:466px}
  .ad-card--portrait{left:309px;top:624px;width:582px;height:466px}
  .size-label{position:absolute;left:0;width:1200px;text-align:center;
    font-family:"Poppins",sans-serif;font-style:italic;font-weight:800;font-size:21px;color:#111;letter-spacing:.3px}
  .size-label--square{top:551px}
  .size-label--portrait{top:1116px}
  .t-firm{font-family:"Jost",sans-serif;font-weight:600;fill:var(--brand-blue)}
  .t-head{font-family:"Jost",sans-serif;font-weight:700;fill:var(--white);text-anchor:middle}
  .t-pill{font-family:"Poppins",sans-serif;font-weight:600;fill:var(--white);text-anchor:middle}
  .t-quote{font-family:"Poppins",sans-serif;font-weight:400;fill:var(--white);text-anchor:middle}
  .quote-mark{fill:none;stroke:var(--quote-line);stroke-width:1.6;stroke-linejoin:round}
  .t-cta-top{font-family:"Jost",sans-serif;font-weight:600;fill:var(--ink)}
  .t-cta-main{font-family:"Jost",sans-serif;font-weight:700;fill:var(--brand-blue)}
  .t-contact{font-family:"Poppins",sans-serif;font-weight:600;fill:#111}
  .icon{fill:none;stroke:var(--brand-blue);stroke-width:2;stroke-linecap:round;stroke-linejoin:round}
</style>
</head>
<body>
<svg width="0" height="0" style="position:absolute" aria-hidden="true">
  <defs>
    <symbol id="quote-open" viewBox="0 0 32 26">
      <path vector-effect="non-scaling-stroke" d="M2,25 L5,11 C6,5 9,2 14,1 L13,5 C10,6 9,8 8.5,11 L11,11 L8,25 Z"/>
      <path vector-effect="non-scaling-stroke" d="M17,25 L20,11 C21,5 24,2 29,1 L28,5 C25,6 24,8 23.5,11 L26,11 L23,25 Z"/>
    </symbol>
    <symbol id="quote-close" viewBox="0 0 32 26">
      <g transform="rotate(180 16 13)">
        <path vector-effect="non-scaling-stroke" d="M2,25 L5,11 C6,5 9,2 14,1 L13,5 C10,6 9,8 8.5,11 L11,11 L8,25 Z"/>
        <path vector-effect="non-scaling-stroke" d="M17,25 L20,11 C21,5 24,2 29,1 L28,5 C25,6 24,8 23.5,11 L26,11 L23,25 Z"/>
      </g>
    </symbol>
  </defs>
</svg>
<main class="board">

  <!-- 1:1 ad -->
  <section class="ad-card ad-card--square">
    <svg viewBox="0 0 750 751" xmlns="http://www.w3.org/2000/svg">
      <defs>
        <linearGradient id="sqBlue" x1="0" y1="0" x2="0.4" y2="1">
          <stop offset="0" stop-color="var(--navy-deep)"/>
          <stop offset="1" stop-color="var(--navy)"/>
        </linearGradient>
        <linearGradient id="sqPhotoGrey" x1="0" y1="0" x2="0" y2="1">
          <stop offset="0" stop-color="var(--photo-light)"/>
          <stop offset="1" stop-color="var(--photo-dark)"/>
        </linearGradient>
        <linearGradient id="sqTeam" x1="0" y1="0" x2="0" y2="1">
          <stop offset="0" stop-color="#2a2f8a"/>
          <stop offset="1" stop-color="#3d4360"/>
        </linearGradient>
        <clipPath id="sqBlueClip">
          <path d="M247,0 H750 V455 A300 300 0 0 1 247 480 Z"/>
        </clipPath>
      </defs>

      <rect class="ad-bg" width="750" height="751" fill="var(--white)"/>
      <path class="accent-lavender" d="M495,751 A300 300 0 0 1 750 440 V751 Z" fill="var(--lavender)"/>
      <path class="panel-blue" d="M247,0 H750 V455 A300 300 0 0 1 247 480 Z" fill="url(#sqBlue)"/>

      <text class="t-firm" x="125" y="82" font-size="19" text-anchor="middle">Lindqvist Harrow,</text>
      <text class="t-firm" x="125" y="104" font-size="19" text-anchor="middle">P.A.</text>

      <rect class="photo-homeowner" x="38" y="136" width="267" height="441" rx="133" fill="url(#sqPhotoGrey)"
            role="img" aria-label="Black and white photo of a stressed homeowner sitting with his head in his hands"/>

      <text class="t-head" x="509" y="70" font-size="38">HOA VIOLATING</text>
      <text class="t-head" x="503" y="138" font-size="80">YOUR</text>
      <text class="t-head" x="509" y="206" font-size="82">RIGHTS?</text>

      <rect class="pill" x="317" y="227" width="385" height="29" rx="2" fill="var(--pill)"/>
      <text class="t-pill" x="509" y="247" font-size="15.5" letter-spacing="2.6">WE SUE HOAS FOR HOMEOWNERS</text>

      <use class="quote-mark" href="#quote-open" x="320" y="274" width="30" height="24"/>
      <text class="t-quote" x="509" y="292" font-size="19">Serving Homeowners in Florida</text>
      <text class="t-quote" x="509" y="315" font-size="19">with our main office in</text>
      <text class="t-quote" x="509" y="338" font-size="19">Miami-Dade.</text>
      <use class="quote-mark" href="#quote-close" x="593" y="330" width="30" height="24"/>

      <g clip-path="url(#sqBlueClip)">
        <rect class="photo-attorneys" x="287" y="370" width="402" height="270" rx="40" fill="url(#sqTeam)"
              role="img" aria-label="Portrait photo of the two firm attorneys in suits"/>
      </g>

      <text class="t-cta-top" x="38" y="681" font-size="22">CONTACT US TODAY FOR</text>
      <text class="t-cta-main" x="38" y="715" font-size="30">A CONSULTATION!</text>

      <path class="icon" d="M351,667 l4,-2 3,5 -2,2 c1,3 3,5 6,6 l2,-2 5,3 -2,4 c-8,0 -16,-8 -16,-16 z"/>
      <text class="t-contact" x="377" y="681" font-size="21">1-800-555-0142</text>
      <g class="icon">
        <circle cx="359" cy="708" r="8"/>
        <ellipse cx="359" cy="708" rx="3.5" ry="8"/>
        <line x1="351" y1="708" x2="367" y2="708"/>
      </g>
      <text class="t-contact" x="377" y="715" font-size="18.5">www.brightgatelegal-example.com</text>
    </svg>
  </section>
  <p class="size-label size-label--square">1080 X 1080 PIXELS</p>

  <!-- 4:5 ad -->
  <section class="ad-card ad-card--portrait">
    <svg viewBox="0 0 937 751" xmlns="http://www.w3.org/2000/svg">
      <defs>
        <linearGradient id="ptBlue" x1="0" y1="0" x2="0.4" y2="1">
          <stop offset="0" stop-color="var(--navy-deep)"/>
          <stop offset="1" stop-color="var(--navy)"/>
        </linearGradient>
        <linearGradient id="ptPhotoGrey" x1="0" y1="0" x2="0" y2="1">
          <stop offset="0" stop-color="var(--photo-light)"/>
          <stop offset="1" stop-color="var(--photo-dark)"/>
        </linearGradient>
        <linearGradient id="ptTeam" x1="0" y1="0" x2="0" y2="1">
          <stop offset="0" stop-color="#2a2f8a"/>
          <stop offset="1" stop-color="#3d4360"/>
        </linearGradient>
        <clipPath id="ptBlueClip">
          <path d="M318,0 H937 V462 A360 360 0 0 1 318 500 Z"/>
        </clipPath>
      </defs>

      <rect class="ad-bg" width="937" height="751" fill="var(--white)"/>
      <path class="accent-lavender" d="M722,751 A330 330 0 0 1 937 450 V751 Z" fill="var(--lavender)"/>
      <path class="panel-blue" d="M318,0 H937 V462 A360 360 0 0 1 318 500 Z" fill="url(#ptBlue)"/>

      <text class="t-firm" x="207" y="84" font-size="21" text-anchor="middle">Lindqvist Harrow,</text>
      <text class="t-firm" x="207" y="108" font-size="21" text-anchor="middle">P.A.</text>

      <rect class="photo-homeowner" x="59" y="136" width="330" height="492" rx="165" fill="url(#ptPhotoGrey)"
            role="img" aria-label="Black and white photo of a stressed homeowner sitting with his head in his hands"/>

      <text class="t-head" x="633" y="72" font-size="42">HOA VIOLATING</text>
      <text class="t-head" x="627" y="148" font-size="86">YOUR</text>
      <text class="t-head" x="633" y="224" font-size="88">RIGHTS?</text>

      <rect class="pill" x="422" y="242" width="423" height="32" rx="2" fill="var(--pill)"/>
      <text class="t-pill" x="633" y="265" font-size="17" letter-spacing="2.8">WE SUE HOAS FOR HOMEOWNERS</text>

      <use class="quote-mark" href="#quote-open" x="426" y="294" width="34" height="27"/>
      <text class="t-quote" x="633" y="316" font-size="22">Serving Homeowners in Florida</text>
      <text class="t-quote" x="633" y="342" font-size="22">with our main office in</text>
      <text class="t-quote" x="633" y="368" font-size="22">Miami-Dade.</text>
      <use class="quote-mark" href="#quote-close" x="728" y="355" width="34" height="27"/>

      <g clip-path="url(#ptBlueClip)">
        <rect class="photo-attorneys" x="427" y="391" width="410" height="290" rx="40" fill="url(#ptTeam)"
              role="img" aria-label="Portrait photo of the two firm attorneys in suits"/>
      </g>

      <text class="t-cta-top" x="60" y="677" font-size="22">CONTACT US TODAY FOR</text>
      <text class="t-cta-main" x="60" y="710" font-size="30">A CONSULTATION!</text>

      <path class="icon" d="M348,695 l4,-2 3,5 -2,2 c1,3 3,5 6,6 l2,-2 5,3 -2,4 c-8,0 -16,-8 -16,-16 z"/>
      <text class="t-contact" x="372" y="710" font-size="20">1-800-555-0142</text>
      <g class="icon">
        <circle cx="564" cy="703" r="8"/>
        <ellipse cx="564" cy="703" rx="3.5" ry="8"/>
        <line x1="556" y1="703" x2="572" y2="703"/>
      </g>
      <text class="t-contact" x="580" y="709" font-size="18">www.brightgatelegal-example.com</text>
    </svg>
  </section>
  <p class="size-label size-label--portrait">1080 X 1350 PIXELS</p>

</main>
</body>
</html>
```